The Lantern Protocol: A Practical Guide for Tending Old Orchards

This will be for both the hard cover and paperback version. A core theme of the book and what we want to cover to convey is the journey or transformation to "happiness". Concepts such as road/pathway, mountain top, sunrise, dark to bright colors, out-of-focus to in-focus, clouds parting, etc., all represent this idea. I am attaching a 1-page book summary for more information. I like the idea of the subtitle being in a gold seal, but that is not necessary. I am open to any designs, but it should at least be conceptually related to the book.

```html
<!DOCTYPE html>
<html lang="en">
<head>
<meta charset="utf-8">
<title>The Lantern Protocol — Cover</title>
<link rel="stylesheet" href="https://fonts.googleapis.com/css2?family=Anton&family=Comic+Neue:wght@700&family=Open+Sans:wght@300&family=Playfair+Display:wght@900&display=swap">
<style>
  :root {
    --page-bg: #ebebeb;
    --night: #141829;
    --night-teal: #1f3440;
    --dusk-violet: #3a2640;
    --ember: #e0612a;
    --amber: #f4a623;
    --sun: #fbe6a2;
    --ink-white: #ffffff;
    --band-gold: #f7c61d;
    --band-ink: #1b1b1b;
  }
  * { margin: 0; padding: 0; box-sizing: border-box; }
  html, body {
    width: 1200px;
    height: 622px;
    overflow: hidden;
    background: var(--page-bg);
  }
  .canvas {
    position: relative;
    width: 1200px;
    height: 622px;
  }
  .cover {
    position: absolute;
    left: 405px;
    top: 35px;
    width: 390px;
    height: 552px;
    overflow: hidden;
    background: var(--night);
    box-shadow: 0 4px 14px rgba(0,0,0,0.12);
  }
  .cover-art {
    position: absolute;
    inset: 0;
    width: 100%;
    height: 100%;
  }
  .title-block {
    position: absolute;
    left: 0;
    right: 0;
    top: 22px;
    text-align: center;
    color: var(--ink-white);
  }
  .title-the {
    font-family: "Playfair Display", serif;
    font-weight: 900;
    font-size: 58px;
    line-height: 1;
    letter-spacing: 0.02em;
  }
  .title-main {
    font-family: "Anton", sans-serif;
    font-size: 86px;
    line-height: 0.95;
    margin-top: -2px;
    letter-spacing: 0.01em;
  }
  .title-sub {
    font-family: "Anton", sans-serif;
    font-size: 24px;
    line-height: 1;
    letter-spacing: 0.42em;
    margin-top: 4px;
    padding-left: 0.42em;
  }
  .subtitle-band {
    position: absolute;
    left: 24px;
    width: 342px;
    top: 216px;
    height: 17px;
    background: var(--band-gold);
    color: var(--band-ink);
    font-family: "Comic Neue", cursive;
    font-weight: 700;
    font-size: 12.5px;
    line-height: 17px;
    text-align: center;
    white-space: nowrap;
  }
  .author {
    position: absolute;
    left: 0;
    right: 0;
    bottom: 22px;
    text-align: center;
    color: var(--ink-white);
    font-family: "Open Sans", sans-serif;
    font-weight: 300;
    font-size: 29px;
    letter-spacing: 0.22em;
    padding-left: 0.22em;
    line-height: 1;
  }
</style>
</head>
<body>
  <main class="canvas">
    <article class="cover">
      <svg class="cover-art" viewBox="0 0 390 552" preserveAspectRatio="none" role="img" aria-label="Painted illustration: a lone figure standing on still water facing a large setting sun between dark violet clouds, with golden light reflected across the water">
        <defs>
          <linearGradient id="sky-to-water" x1="0" y1="0" x2="0" y2="1">
            <stop offset="0" stop-color="var(--night)"/>
            <stop offset="0.22" stop-color="var(--night-teal)"/>
            <stop offset="0.36" stop-color="var(--dusk-violet)"/>
            <stop offset="0.5" stop-color="var(--ember)"/>
            <stop offset="0.6" stop-color="var(--dusk-violet)"/>
            <stop offset="0.78" stop-color="var(--night)"/>
            <stop offset="1" stop-color="var(--night-teal)"/>
          </linearGradient>
          <radialGradient id="sun-glow" cx="0.5" cy="0.55" r="0.42">
            <stop offset="0" stop-color="var(--sun)"/>
            <stop offset="0.3" stop-color="var(--amber)" stop-opacity="0.9"/>
            <stop offset="0.65" stop-color="var(--ember)" stop-opacity="0.35"/>
            <stop offset="1" stop-color="var(--ember)" stop-opacity="0"/>
          </radialGradient>
        </defs>
        <rect class="art-base" width="390" height="552" fill="url(#sky-to-water)"/>
        <rect class="art-glow" width="390" height="552" fill="url(#sun-glow)"/>
      </svg>

      <header class="title-block">
        <h1>
          <span class="title-the" style="display:block">THE</span>
          <span class="title-main" style="display:block">LANTERN</span>
          <span class="title-sub" style="display:block">PROTOCOL</span>
        </h1>
      </header>

      <p class="subtitle-band">A Practical Guide for Tending Old Orchards</p>

      <p class="author">DANA R. WHITLOW</p>
    </article>
  </main>
</body>
</html>
```